Plakat-Design für Coding Challenge
Zielgruppe
Die KORVAMID.IO GmbH entwickelt individuelle Software Entwicklung im Web- & mobile Bereich. Im Rahmen einer angesetzten Coding-Challenge, die über den Zeitraum von ca. 6 Wochen läuft, sollen potentielle Kandidaten (primär Studenten) zur Teilnahme aufgefordert werden.
Aufgabenstellung
Es gibt bereits unter der URL https://wettbewerb.korvamid.example eine Webseite, auf der die Details zur anstehenden Challenge gelistet sind.
Um die Zielgruppe via Aushang anzusprechen, sollen vom Styling/Layout passende DIN-A2 Plakate entworfen werden.
Gerne kann auf die Gewinne hingewiesen werden. Bitte Platz für einen QR-Code vorsehen, welcher auf die o.g. Seite verlinkt.
Entwürfe bis 27.11.2017 - 18:00 Uhr können berücksichtigt werden

```html
<!DOCTYPE html>
<html lang="de">
<head>
<meta charset="utf-8">
<title>KORVAMID.IO Coding Challenge – Plakat</title>
<link rel="stylesheet" href="https://fonts.googleapis.com/css2?family=Courier+Prime:wght@400;700&family=Open+Sans:wght@300;400;600;700&display=swap">
<style>
  :root {
    --ink: #000000;
    --paper: #ffffff;
    --accent: #0a9ae0;
    --grid-tone: #3a3a3a;
    --sans: "Open Sans", Arial, sans-serif;
    --mono: "Courier Prime", "Courier New", monospace;
  }
  html, body {
    margin: 0;
    padding: 0;
    width: 848px;
    height: 1200px;
    overflow: hidden;
    background: var(--ink);
  }
  .poster {
    position: relative;
    width: 848px;
    height: 1200px;
    overflow: hidden;
    background: var(--ink);
    font-family: var(--sans);
    color: var(--paper);
  }
  .pixel-field {
    position: absolute;
    left: 0;
    top: 0;
    width: 848px;
    height: 900px;
    background:
      radial-gradient(ellipse 70% 55% at 55% 35%, rgba(120,120,120,0.35), rgba(60,60,60,0.18) 55%, rgba(0,0,0,0) 100%),
      linear-gradient(to bottom, #1e1e1e 0%, #161616 60%, var(--ink) 100%);
  }
  .prize-ribbon {
    position: absolute;
    top: 0;
    left: 0;
    width: 848px;
    height: 400px;
  }
  .prize-ribbon__text {
    position: absolute;
    left: 560px;
    top: 122px;
    width: 300px;
    transform: rotate(45deg);
    transform-origin: center;
    text-align: center;
    font-size: 24px;
    font-weight: 600;
    line-height: 31px;
    color: var(--paper);
  }
  .brand {
    position: absolute;
    left: 62px;
    top: 272px;
    margin: 0;
    font-family: var(--sans);
    font-weight: 600;
    font-size: 52px;
    letter-spacing: 1px;
    line-height: 1;
  }
  .headline {
    position: absolute;
    left: 50px;
    top: 340px;
    margin: 0;
    font-family: var(--mono);
    font-weight: 400;
    font-size: 106px;
    line-height: 92px;
    letter-spacing: 1px;
    -webkit-text-stroke: 2px var(--paper);
  }
  .headline span { display: block; }
  .teaser {
    position: absolute;
    left: 50px;
    top: 564px;
    width: 534px;
    height: 206px;
    box-sizing: border-box;
    padding: 13px 16px;
    background: var(--accent);
    clip-path: polygon(0 0, 100% 0, 100% 137px, 468px 100%, 0 100%);
    font-size: 17.5px;
    line-height: 25px;
    font-weight: 400;
  }
  .teaser__title {
    margin: 0;
    font-weight: 700;
    font-size: 17px;
    text-transform: uppercase;
  }
  .teaser p { margin: 0; }
  .teaser__more { margin-top: 24px !important; }
  .teaser__link { font-weight: 700; }
  .qr-space {
    position: absolute;
    left: 679px;
    top: 1036px;
    width: 137px;
    height: 135px;
    background: var(--paper);
  }
  .footer-url {
    position: absolute;
    right: 210px;
    top: 1146px;
    margin: 0;
    font-size: 24px;
    font-weight: 600;
    color: var(--accent);
    line-height: 1;
  }
</style>
</head>
<body>
<main class="poster">
  <div class="pixel-field" role="img" aria-label="Dunkles Raster aus kleinen grauen Pixelquadraten"></div>

  <svg class="prize-ribbon" width="848" height="400" viewBox="0 0 848 400" aria-hidden="true">
    <polygon points="491,0 600,0 848,248 848,358" fill="var(--accent)"/>
  </svg>
  <div class="prize-ribbon__text">Preise im Gesamtwert<br>von 1.300 € zu gewinnen!</div>

  <h2 class="brand">KORVAMID.IO</h2>
  <h1 class="headline"><span>&lt;CODING</span><span>CHALLENGE/&gt;</span></h1>

  <section class="teaser">
    <h3 class="teaser__title">Vorlesungen sind dir nicht genug?</h3>
    <p>Du brauchst Abwechslung oder willst zeigen, wie Du es mit Problemen aus der echten Welt aufnimmst? Dann mach mit!</p>
    <p class="teaser__more">Alle Infos unter:<br><span class="teaser__link">https://wettbewerb.korvamid.example</span></p>
  </section>

  <div class="qr-space" aria-label="Platz für QR-Code"></div>
  <p class="footer-url">https://wettbewerb.korvamid.example</p>
</main>
</body>
</html>
```